Label Design for RTD Cocktail Line Tolvanu Cellars

Tolvanu Cellars is a line of Indian-inspired artisan cocktails that "brings the bartender home" for professional men and women who like the finer things in life but don’t always have the time to treat themselves. No need for a multitude of expensive and hard-to-find ingredients, time consuming recipes, or a mixologist.

Our line of 3 open and serve cocktails blends a range of premium spirits with exotic ingredients so you can conveniently raise a glass for any of life’s celebrations.

Our bottle is the 750ml Claret bottle with Quorlex (screw cap) closure and will be covered entirely in a shrink sleeve (so potentially anything can be designed for any part of the bottle). We want the bottle to pop on the shelf so it should look different than what’s already out there (Velvet Fawn, Korvadel, Mirelda ready to drink cocktails). We are looking for a sexy design that's polished/sleek.
Updates

Reason: Hello designers! Tolvanu Cellars is so impressed with what we have received thus far and we would like to give some of the designers a few extra days to make the edits we requested. It's never too late to submit! Thank you all!

Requirements
Must have
• Front of bottle
* “Tolvanu Cellars” name and Peacock Logo- but feel free to pull the elements apart and use them on the bottle in different ways
* Open & Serve
* 12% ALC/VOL
* 750 ml
* 3 different labels in a theme for
-Brovanza
-Zestrovino
-Florquena

Brovanza Ideas- soft brown palate, the ingredients in chai spice (cloves, cardamom pods, nutmeg, black peppercorns, star anise, and cinnamon stick)

Zestrovino Ideas -cool and refreshing, pale green shade (not clashing with logo), graphics of fresh mint leaves, green chili, lime, cucumber

Florquena Ideas- soft/pale pink shades, graphics of lychi fruit (outer red shell and inner pink flesh), ginger

Back of bottle
* explanation of the 3 cocktails
Brovanza: Forget what you think you know about chai, this is not the Queen’s tea-time drink! Brovanza is a smooth, sweetly -spiced cocktail made with vodka, black tea, and a combination of aromatic spices. This velvety cocktail is rich without being heavy. Enjoy chilled or over ice anytime.

Zestrovino: Zestrovino can’t make up its mind! This fusion of zesty lime, sweet mint, earthy cucumber and spicy chilies is so refreshing you’ll crave it on a hot summer day or a cool winter’s night. The exotic botanicals in gin add a complexity to the cocktail making this a refreshing but potent drink! Enjoy chilled or over ice anytime.

Florquena: East meet West. Delicate lychi meet hard-hitting whiskey. Florquena will tempt you senses with flavor, fragrance and beauty. The peppery kick of ginger and the intensity of the un-aged whiskey are softened by lychi’s intoxicating scent and subtle, sweet finish.

Please include
1. Bottled By PQR Spirits Company
2. Sample barcode (where you would place it in your design)
3. www.TolvanuCellars.example
4. GOVERNMENT WARNING: (1) According to the Surgeon General, women should not drink alcoholic beverages during pregnancy because of the risk of birth defects. (2) Consumption of alcoholic beverages impairs your ability to drive a car or operate machinery, and may cause health problems.

Optional to include
*"Bring the Bartender Home"
*"Tolvanu Cellars” name and Peacock Logo on the back
*Entirely black sleeve with contrasting design

FYI the Fonts used in our logo are Geosans Light and Prakrta, but feel free to use other complimentary fonts on the other aspects.
Nice to have
• Optional to include

```html
<!DOCTYPE html>
<html lang="en">
<head>
<meta charset="utf-8">
<title>Tolvanu Cellars – Label Design</title>
<link rel="stylesheet" href="https://fonts.googleapis.com/css2?family=Cormorant+Garamond:ital,wght@0,400;0,600;1,400;1,600&family=Josefin+Sans:wght@600&family=Open+Sans:wght@400&display=swap">
<style>
  :root {
    --page: #ffffff;
    --label-white: #fbfbfb;
    --chai-red: #b8161a;
    --chai-deep: #7d0d0e;
    --mirchi-blue: #1f6f9f;
    --mirchi-deep: #143f78;
    --mirchi-light: #7fc2de;
    --gold: #c9962e;
    --gold-light: #f0d27a;
    --logo-teal: #1d7fa0;
    --ink-navy: #1c2f66;
    --panel-text: #f2f7fb;
  }
  * { margin: 0; padding: 0; box-sizing: border-box; }
  html, body { width: 901px; height: 1200px; overflow: hidden; background: var(--page); }
  .canvas { position: relative; width: 901px; height: 1200px; }
  .artwork { position: absolute; inset: 0; }
  .brand-mark { font-family: "Josefin Sans", sans-serif; font-weight: 600; fill: var(--logo-teal); }
  .product-name { font-family: "Josefin Sans", sans-serif; font-weight: 600; }
  .flavour { font-family: "Cormorant Garamond", serif; font-style: italic; }
  .abv { font-family: "Open Sans", sans-serif; }
  .volume { font-family: "Cormorant Garamond", serif; font-style: italic; font-weight: 600; }

  .panel-copy {
    position: absolute;
    font-family: "Cormorant Garamond", serif;
    color: var(--panel-text);
  }
  .panel-copy--info { left: 408px; top: 904px; width: 150px; font-size: 7.5px; font-style: italic; line-height: 1.35; }
  .panel-copy--info li { list-style: none; margin-bottom: 11px; }
  .panel-copy--story { left: 590px; top: 900px; width: 146px; }
  .panel-copy--story h3 { font-style: italic; font-weight: 400; font-size: 14px; margin-bottom: 4px; }
  .panel-copy--story .description { font-style: italic; font-size: 7px; line-height: 1.35; margin-bottom: 10px; }
  .panel-copy--story .warning { font-size: 7px; line-height: 1.35; }
  .panel-url {
    position: absolute; left: 466px; top: 1073px;
    font-family: "Cormorant Garamond", serif; font-style: italic; font-size: 6.5px; color: var(--panel-text);
  }
</style>
</head>
<body>
<main class="canvas">
  <svg class="artwork" width="901" height="1200" viewBox="0 0 901 1200" xmlns="http://www.w3.org/2000/svg">
    <defs>
      <linearGradient id="chai-swoosh" x1="0" y1="0" x2="1" y2="0">
        <stop offset="0" stop-color="var(--chai-deep)"/>
        <stop offset="0.5" stop-color="var(--chai-red)"/>
        <stop offset="1" stop-color="#e6504a"/>
      </linearGradient>
      <linearGradient id="mirchi-swoosh" x1="0" y1="0" x2="1" y2="0">
        <stop offset="0" stop-color="var(--mirchi-deep)"/>
        <stop offset="0.6" stop-color="var(--mirchi-blue)"/>
        <stop offset="1" stop-color="var(--mirchi-light)"/>
      </linearGradient>
      <linearGradient id="panel-fill" x1="0" y1="0" x2="0" y2="1">
        <stop offset="0" stop-color="#1d4f8e"/>
        <stop offset="0.6" stop-color="#2a6fa5"/>
        <stop offset="1" stop-color="#5fa7cf"/>
      </linearGradient>
      <linearGradient id="gold-ribbon" x1="0" y1="0" x2="1" y2="0">
        <stop offset="0" stop-color="var(--gold)"/>
        <stop offset="0.5" stop-color="var(--gold-light)"/>
        <stop offset="1" stop-color="var(--gold)"/>
      </linearGradient>
    </defs>

    <g class="front-label front-label--brovanza" transform="translate(241 425)">
      <rect width="172" height="257" fill="var(--label-white)"/>
      <path d="M0 0 H22 C8 35 30 70 20 105 C10 140 8 175 28 200 C20 215 10 225 0 232 Z" fill="url(#chai-swoosh)"/>
      <path d="M0 257 V232 C40 215 80 218 120 232 C145 240 160 236 172 228 V257 Z" fill="url(#chai-swoosh)"/>
      <path d="M60 240 C100 224 140 226 172 214 V220 C140 232 100 232 60 240 Z" fill="var(--gold)"/>
      <circle cx="110" cy="45" r="9" fill="var(--logo-teal)"/>
      <text class="brand-mark" x="110" y="73" font-size="11" text-anchor="middle">Tolvanu Cellars</text>
      <text class="product-name" x="106" y="135" font-size="26" text-anchor="middle" fill="var(--logo-teal)">Tolvanu</text>
      <text class="flavour" x="156" y="153" font-size="14" text-anchor="end" fill="var(--chai-red)">Brovanza</text>
      <text class="abv" x="31" y="211" font-size="8" fill="var(--chai-deep)">12% ALC/VOL</text>
      <text class="volume" x="110" y="212" font-size="16" fill="var(--chai-deep)">750 ml</text>
    </g>

    <g class="front-label front-label--zestrovino" transform="translate(491 425)">
      <rect width="170" height="257" fill="var(--label-white)"/>
      <path d="M0 0 H22 C8 35 30 70 20 105 C10 140 8 175 28 200 C20 215 10 225 0 232 Z" fill="url(#mirchi-swoosh)"/>
      <path d="M0 257 V232 C40 215 80 218 120 232 C145 240 160 236 170 228 V257 Z" fill="url(#mirchi-swoosh)"/>
      <path d="M60 240 C100 224 140 226 170 214 V220 C140 232 100 232 60 240 Z" fill="var(--gold)"/>
      <circle cx="88" cy="45" r="9" fill="var(--logo-teal)"/>
      <text class="brand-mark" x="88" y="73" font-size="11" text-anchor="middle">Tolvanu Cellars</text>
      <text class="product-name" x="88" y="135" font-size="26" text-anchor="middle" fill="var(--logo-teal)">Tolvanu</text>
      <text class="flavour" x="138" y="153" font-size="14" text-anchor="end" fill="var(--ink-navy)">Zestrovino</text>
      <text class="abv" x="24" y="211" font-size="8" fill="var(--ink-navy)">12% ALC/VOL</text>
      <text class="volume" x="106" y="212" font-size="16" fill="var(--ink-navy)">750 ml</text>
    </g>

    <g class="sleeve" transform="translate(195 845)">
      <rect width="562" height="268" fill="var(--label-white)"/>
      <path d="M0 0 H34 C14 40 40 80 28 125 C16 170 14 205 36 232 C22 248 10 258 0 262 Z" fill="url(#mirchi-swoosh)"/>
      <path d="M0 268 V250 C80 222 160 226 250 246 C330 262 420 250 562 218 V268 Z" fill="url(#mirchi-swoosh)"/>
      <path d="M150 262 C230 226 300 214 370 180 C410 160 440 150 470 156 C510 164 540 170 562 160 V168 C540 180 510 174 470 166 C440 160 410 172 370 192 C300 226 230 240 150 262 Z" fill="url(#gold-ribbon)"/>
      <rect x="195" y="53" width="177" height="190" rx="9" fill="url(#panel-fill)" fill-opacity="0.93" stroke="#d6e8f3" stroke-width="1"/>
      <rect x="385" y="53" width="162" height="190" rx="9" fill="url(#panel-fill)" fill-opacity="0.93" stroke="#d6e8f3" stroke-width="1"/>
      <circle cx="95" cy="40" r="10" fill="var(--logo-teal)"/>
      <text class="brand-mark" x="95" y="70" font-size="12" text-anchor="middle">Tolvanu Cellars</text>
      <text class="product-name" x="96" y="145" font-size="30" text-anchor="middle" fill="var(--logo-teal)">Tolvanu</text>
      <text class="flavour" x="166" y="165" font-size="15" text-anchor="end" fill="var(--ink-navy)">Zestrovino</text>
      <text class="abv" x="42" y="230" font-size="8.5" fill="var(--ink-navy)">12% ALC/VOL</text>
      <text class="volume" x="112" y="230" font-size="17" fill="var(--ink-navy)">750 ml</text>
    </g>
  </svg>

  <ol class="panel-copy panel-copy--info">
    <li>1. Enjoy responsibly</li>
    <li>2. Bottled By PQR Spirits Company</li>
    <li>3. Sample barcode (where you would place it in your design)</li>
    <li>4. www.TolvanuCellars.example</li>
  </ol>
  <p class="panel-url">www.TolvanuCellars.example</p>

  <div class="panel-copy panel-copy--story">
    <h3>Zestrovino</h3>
    <p class="description">2. Zestrovino description: Zestrovino can’t make up its mind! This fusion of zesty lime, sweet mint, earthy cucumber and spicy chilies is so refreshing you’ll crave it on a hot summer day or a cool winter’s night. The exotic botanicals in gin add a complexity to the cocktail making this a refreshing but potent drink! Enjoy chilled or over ice anytime.</p>
    <p class="warning">GOVERNMENT WARNING: (1) According to the Surgeon General, women should not drink alcoholic beverages during pregnancy because of the risk of birth defects. (2) Consumption of alcoholic beverages impairs your ability to drive a car or operate machinery, and may cause health problems.</p>
  </div>
</main>
</body>
</html>
```